Criação de Papelaria Profissional para Tecnologia & Ciencias
A empresa queria:
" Atuamos no mercado nacional distribuindo conectividade através de Chips M2M, além de Plataforma de Rastreamento Veicular e soluções em IoT. "

```html
<!DOCTYPE html>
<html lang="pt-BR">
<head>
<meta charset="UTF-8">
<title>Velquio – Crachá e Cordão</title>
<link rel="stylesheet" href="https://fonts.googleapis.com/css2?family=Montserrat:wght@400;500;800&family=Roboto:wght@400;500&display=swap">
<style>
  :root {
    --mint: #79d9c4;
    --mint-deep: #5fc8b2;
    --ink: #1d1d1d;
    --charcoal: #2c2c2c;
    --graphite: #4a4a4a;
    --paper: #ffffff;
    --stage: #efefef;
    --line: #222222;
  }
  * { box-sizing: border-box; margin: 0; padding: 0; }
  html, body { width: 1200px; height: 1200px; overflow: hidden; }
  body {
    background: var(--stage);
    font-family: "Roboto", Arial, sans-serif;
    position: relative;
  }

  /* Lanyard strap */
  .strap {
    position: absolute;
    left: 60px; top: 90px;
    width: 1080px; height: 110px;
    background: var(--mint);
    display: flex; align-items: center;
    overflow: hidden;
  }
  .strap-pattern {
    width: 170px; height: 100%;
    flex-shrink: 0;
    background: linear-gradient(90deg, var(--ink) 0%, var(--mint-deep) 60%, var(--mint) 100%);
  }
  .strap-pattern.end {
    background: linear-gradient(270deg, var(--ink) 0%, var(--mint-deep) 60%, var(--mint) 100%);
  }
  .strap-brands {
    flex: 1;
    display: flex; justify-content: space-around; align-items: center;
  }
  .brand-name {
    font-family: "Montserrat", Arial, sans-serif;
    font-weight: 800; letter-spacing: -0.5px;
  }
  .strap-brand { font-size: 30px; color: var(--ink); }

  /* Cards */
  .card {
    position: absolute;
    top: 280px;
    width: 460px; height: 840px;
    overflow: hidden;
  }
  .card-front { left: 110px; background: var(--charcoal); }
  .card-back  { left: 630px; background: var(--paper); border: 1px solid #dcdcdc; }

  .slot {
    position: absolute; left: 50%; top: 26px;
    width: 120px; height: 20px; margin-left: -60px;
    border-radius: 10px;
  }
  .card-front .slot { background: #d9d9d9; }
  .card-back .slot { background: var(--mint); }

  .front-curves { position: absolute; inset: 0; }

  .front-logo {
    position: absolute; left: 0; right: 0; top: 100px;
    text-align: center;
    font-size: 44px; color: var(--paper);
  }

  .photo {
    position: absolute; left: 110px; top: 260px;
    width: 240px; height: 300px;
    background: linear-gradient(180deg, #cfcfcf 0%, #9a7a66 55%, #6b4a3a 100%);
    border: 4px solid var(--paper);
  }

  .holder-name {
    position: absolute; left: 0; right: 0; top: 600px;
    text-align: center;
    font-family: "Montserrat", Arial, sans-serif;
    font-weight: 500; font-size: 54px; line-height: 1.1; color: var(--mint);
  }
  .holder-role {
    position: absolute; left: 0; right: 0; top: 672px;
    text-align: center;
    font-family: "Montserrat", Arial, sans-serif;
    font-size: 30px; color: var(--paper);
  }

  /* Back */
  .back-logo {
    position: absolute; left: 0; right: 0; top: 110px;
    text-align: center;
    font-size: 44px; color: var(--ink);
  }

  .fields {
    position: absolute; left: 42px; right: 42px; top: 270px;
    display: flex; flex-direction: column; gap: 20px;
  }
  .field {
    height: 56px;
    border: 2px solid var(--line); border-radius: 8px;
    padding: 6px 12px;
    font-size: 18px; color: var(--mint-deep);
  }

  .notice {
    position: absolute; left: 60px; right: 60px; top: 540px;
    text-align: center; font-size: 16px; line-height: 1.35; color: var(--ink);
  }
  .notice p + p { margin-top: 18px; }

  .back-band {
    position: absolute; left: 0; right: 0; bottom: 0;
    height: 70px; background: var(--mint);
  }
</style>
</head>
<body>

  <div class="strap">
    <div class="strap-pattern" role="img" aria-label="Padrão de listras onduladas pretas sobre verde-menta"></div>
    <div class="strap-brands">
      <span class="strap-brand brand-name">Velquio</span>
      <span class="strap-brand brand-name">Velquio</span>
      <span class="strap-brand brand-name">Velquio</span>
    </div>
    <div class="strap-pattern end" role="img" aria-label="Padrão de listras onduladas pretas sobre verde-menta"></div>
  </div>

  <section class="card card-front">
    <svg class="front-curves" viewBox="0 0 460 840" aria-hidden="true">
      <path d="M0 330 Q0 230 100 230 L360 230 Q460 230 460 330 L460 840 L300 840 L300 560 Q300 480 220 480 L160 480 Q80 480 80 560 L80 840 L0 840 Z" fill="#3a3a3a"/>
      <path d="M0 420 Q60 420 60 500 L60 840 L0 840 Z" fill="#4a4a4a"/>
      <path d="M460 400 Q400 400 400 480 L400 840 L460 840 Z" fill="#4a4a4a"/>
    </svg>
    <div class="slot"></div>
    <div class="front-logo brand-name">Velquio</div>
    <div class="photo" role="img" aria-label="Foto do colaborador"></div>
    <div class="holder-name">Nome</div>
    <div class="holder-role">Cargo</div>
  </section>

  <section class="card card-back">
    <div class="slot"></div>
    <div class="back-logo brand-name">Velquio</div>
    <div class="fields">
      <div class="field">Nome:</div>
      <div class="field">Cpf:</div>
      <div class="field">Função:</div>
    </div>
    <div class="notice">
      <p>Esta identificação é de uso pessoal e intransferível, o funcionário deverá usá-la obrigatoriamente em horário comercial.</p>
      <p>Em caso de perda favor comunicar imediatamente ao Departamento Pessoal da Empresa.</p>
    </div>
    <div class="back-band"></div>
  </section>

</body>
</html>
```